Printing company needs website!

A printing company would like a new professional website (made with wix). Now they don't have a website, but they want a unique, beautiful, clear site. Of course they provide the content themselves, we are now looking for the beautiful design with some mockups. You can see several of their projects on their instagram & facebook.
Www.kwelmast.com/brimvelt and https://www.fotoravel.com/brimvelt.be/ logos are attached.

```html
<!DOCTYPE html>
<html lang="en">
<head>
<meta charset="utf-8">
<title>Brimvelt – Everything is Printable</title>
<link rel="stylesheet" href="https://fonts.googleapis.com/css2?family=Playfair+Display:wght@400;600;700;900&family=Mulish:wght@300;400;600;700&family=Caveat:wght@500&display=swap">
<style>
:root{
  --navy:#141c2b;
  --navy-deep:#10161f;
  --footer:#141414;
  --footer-bar:#1e1e1e;
  --yellow:#f5c518;
  --blue:#1e88d6;
  --blue-dark:#1565a8;
  --ink:#1b1b1b;
  --grey:#555;
  --white:#ffffff;
}
*{margin:0;padding:0;box-sizing:border-box}
html,body{width:1200px;height:4106px;overflow:hidden}
body{font-family:'Mulish',sans-serif;color:var(--ink);background:var(--white);position:relative}
.abs{position:absolute}
.serif{font-family:'Playfair Display',serif}

/* hero */
.hero{position:absolute;left:0;top:0;width:1200px;height:545px;
  background:linear-gradient(90deg,#1d2334 0%,#2a2f45 38%,rgba(120,60,70,.9) 70%,#b8343c 100%);}
.hero-photo{position:absolute;left:0;top:0;width:1200px;height:545px;
  background:radial-gradient(ellipse at 70% 60%,rgba(200,200,205,.35),transparent 55%),radial-gradient(ellipse at 85% 40%,rgba(230,130,40,.35),transparent 30%)}
.brand{position:absolute;left:65px;top:16px;display:flex;align-items:center;gap:10px;color:var(--white)}
.brand-dot{width:34px;height:34px;border-radius:50%;background:var(--yellow)}
.brand-name{font-weight:700;font-size:26px;line-height:1}
.brand-tag{font-size:8px;opacity:.7;margin-top:2px}
.nav{position:absolute;top:22px;left:0;width:1200px;font-size:16px;color:var(--white)}
.nav a{position:absolute;color:inherit;text-decoration:none}
.nav a.active{color:var(--yellow)}
.hero-script{left:65px;top:118px;font-family:'Caveat',cursive;font-size:38px;color:var(--white)}
.hero-title{left:65px;top:160px;font-family:'Playfair Display',serif;font-weight:700;font-size:64px;line-height:72px;color:var(--white)}
.hero-title span{color:var(--yellow)}
.hero-text{left:65px;top:326px;width:500px;font-size:18px;line-height:28px;color:var(--white)}
.btn{display:flex;align-items:center;justify-content:center;background:var(--blue);color:var(--white);font-size:17px}
.hero-btn{left:65px;top:411px;width:164px;height:52px}
.slide-arrow{top:460px;width:36px;height:36px;border-radius:50%;background:rgba(255,255,255,.12);color:var(--white);display:flex;align-items:center;justify-content:center;font-size:18px}

/* intro */
.section-title{position:absolute;left:0;width:1200px;text-align:center;font-family:'Playfair Display',serif;font-weight:700;font-size:58px;line-height:1}
.intro-text{left:70px;top:694px;width:1060px;text-align:center;font-size:19.5px;line-height:28.5px;color:#333}
.video{left:65px;top:838px;width:1070px;height:447px;background:linear-gradient(180deg,#3a3a3a 0%,#1e1e1e 45%,#6a6a6a 75%,#2a2a2a 100%)}
.play{left:563px;top:1024px}

/* services */
.services{position:absolute;left:0;top:1347px;width:1200px;height:470px;background:linear-gradient(90deg,var(--navy) 0%,#222b3b 50%,var(--navy) 100%)}
.service{position:absolute;top:136px;width:240px;text-align:center;color:var(--white)}
.service svg{display:block;margin:0 auto}
.service h3{font-family:'Playfair Display',serif;font-weight:600;font-size:28px;margin-top:26px;white-space:nowrap}
.service p{font-size:17px;line-height:23px;margin-top:12px;padding:0 14px}

/* work */
.work-card{position:absolute;width:260px;text-align:center;font-size:21px;font-weight:600}
.work-card .img{width:260px}
.work-card p{margin-top:20px}

/* team */
.team{position:absolute;left:0;top:2404px;width:1200px;height:521px;background:linear-gradient(100deg,#2a2f24 0%,#1d2a3c 45%,#16213a 100%)}
.member{position:absolute;top:126px;width:257px;text-align:center;color:var(--white)}
.member .img{width:257px;height:264px}
.member h4{font-family:'Playfair Display',serif;font-weight:400;font-size:28px;margin-top:22px}
.member span{font-size:17px}

/* testimonials */
.testi-text{left:75px;top:3068px;width:1050px;text-align:center;font-size:20.5px;line-height:31.5px;color:#333}
.avatar{position:absolute;border-radius:50%}

/* newsletter */
.newsletter{position:absolute;left:0;top:3467px;width:1200px;height:239px;background:radial-gradient(ellipse at 45% 30%,#6a6630 0%,#2f3a47 40%,#1c2b44 100%)}
.nl-title{left:65px;top:46px;font-family:'Playfair Display',serif;font-weight:700;font-size:58px;line-height:56px;color:var(--white)}
.nl-sub{left:65px;top:170px;font-size:19px;color:var(--white)}
.nl-label{left:394px;top:128px;font-size:14px;color:var(--white)}
.nl-line{left:394px;top:151px;width:589px;height:1px;background:rgba(255,255,255,.7)}
.nl-btn{left:983px;top:88px;width:152px;height:52px}

/* footer */
.footer{position:absolute;left:0;top:3706px;width:1200px;height:338px;background:var(--footer);color:var(--white)}
.footer h5{position:absolute;top:56px;font-family:'Playfair Display',serif;font-weight:700;font-size:25px}
.footer .divider{position:absolute;top:56px;width:1px;height:226px;background:#333}
.contact-row{position:absolute;left:65px;display:flex;gap:14px;font-size:18px;line-height:28px}
.contact-row svg{flex:none;margin-top:6px}
.links{position:absolute;left:481px;top:106px;list-style:none;font-size:18px;line-height:37px}
.touch-text{left:755px;top:108px;width:380px;font-size:15.5px;line-height:25px;color:#aaa}
.outline-btn{left:755px;top:190px;width:164px;height:55px;border:1px solid #555;display:flex;align-items:center;justify-content:center;font-size:17px}
.fill-btn{left:931px;top:190px;width:164px;height:55px}
.footer-bar{position:absolute;left:0;top:4044px;width:1200px;height:62px;background:var(--footer-bar);color:#999;font-size:18px}
.footer-bar .copy{position:absolute;left:65px;top:19px}
.footer-bar .copy b{color:var(--white);font-weight:400}
.social{position:absolute;top:10px;width:41px;height:41px;border:1px solid #555}
</style>
</head>
<body>

<header class="hero">
  <div class="hero-photo" role="img" aria-label="Two printers checking freshly printed sheets at a large press"></div>
  <div class="brand">
    <div class="brand-dot"></div>
    <div><div class="brand-name">Brimvelt</div><div class="brand-tag">print it your way</div></div>
  </div>
  <nav class="nav">
    <a class="active" style="left:531px">Home</a>
    <a style="left:657px">About Us</a>
    <a style="left:810px">Work</a>
    <a style="left:931px">Blog</a>
    <a style="left:1044px">Contact Us</a>
  </nav>
  <div class="abs hero-script">Printable where</div>
  <h1 class="abs hero-title">Everything is<br><span>Printable!</span></h1>
  <p class="abs hero-text">We are an online printing company with our own placement service and printing experts!</p>
  <a class="abs btn hero-btn">Get Started</a>
  <div class="abs slide-arrow" style="left:1052px">‹</div>
  <div class="abs slide-arrow" style="left:1095px">›</div>
</header>

<h2 class="section-title" style="top:600px">Unique Printing Slotuions</h2>
<p class="abs intro-text">Sed ut perspiciatis unde omnis iste natus error sit voluptatem accusantium doloremque laudantium, totam rem aperiam, eaque ipsa quae ab illo inventore veritatis et quasi architecto beatae vitae dicta sunt explicabo. Nemo enim ipsam voluptatem quia voluptas sit aspernatur aut odit aut fugit, sed quia consequuntur magni dolores eos qui ratione voluptatem sequi nesciunt.</p>
<div class="abs video" role="img" aria-label="Printing press rollers running paper at speed"></div>
<svg class="abs play" width="74" height="74" viewBox="0 0 74 74"><circle cx="37" cy="37" r="35" fill="none" stroke="#fff" stroke-width="3"/><path d="M31 26 L49 37 L31 48 Z" fill="#fff"/></svg>

<section class="services">
  <h2 class="section-title" style="top:42px;color:var(--white)">What We Do</h2>
  <div class="service" style="left:79px">
    <svg width="130" height="118" viewBox="0 0 130 118"><path d="M30 6 A56 56 0 0 1 72 110" fill="none" stroke="var(--yellow)" stroke-width="20"/><circle cx="58" cy="74" r="36" fill="var(--blue-dark)"/><g fill="none" stroke="#fff" stroke-width="2.5"><rect x="44" y="70" width="28" height="14"/><rect x="49" y="60" width="18" height="10"/><rect x="49" y="80" width="18" height="10"/></g></svg>
    <h3>Digital Printing</h3><p>Sed ut perspiciatis omnis iste natus error sit amet</p>
  </div>
  <div class="service" style="left:347px">
    <svg width="130" height="118" viewBox="0 0 130 118"><path d="M30 6 A56 56 0 0 1 72 110" fill="none" stroke="var(--yellow)" stroke-width="20"/><circle cx="58" cy="74" r="36" fill="var(--blue-dark)"/><g fill="none" stroke="#fff" stroke-width="2.5"><rect x="43" y="60" width="30" height="24"/><path d="M47 80 L55 71 L61 77 L65 73 L70 80"/><path d="M43 88 H73"/></g></svg>
    <h3>Ofset Printing</h3><p>Sed ut perspiciatis omnis iste natus error sit amet</p>
  </div>
  <div class="service" style="left:615px">
    <svg width="130" height="118" viewBox="0 0 130 118"><path d="M30 6 A56 56 0 0 1 72 110" fill="none" stroke="var(--yellow)" stroke-width="20"/><circle cx="58" cy="74" r="36" fill="var(--blue-dark)"/><g fill="none" stroke="#fff" stroke-width="2.5"><rect x="44" y="62" width="26" height="26"/><path d="M50 70 H64 M50 76 H64 M50 82 H58"/><path d="M66 58 L76 68 L68 76"/></g></svg>
    <h3>Design Services</h3><p>Sed ut perspiciatis omnis iste natus error sit amet</p>
  </div>
  <div class="service" style="left:881px">
    <svg width="130" height="118" viewBox="0 0 130 118"><path d="M30 6 A56 56 0 0 1 72 110" fill="none" stroke="var(--yellow)" stroke-width="20"/><circle cx="58" cy="74" r="36" fill="var(--blue-dark)"/><g fill="none" stroke="#fff" stroke-width="2.5"><path d="M50 58 L44 62 L46 72 L50 70 L50 90 L66 90 L66 70 L70 72 L72 62 L66 58 Q58 64 50 58 Z"/></g></svg>
    <h3>Clothing Printing</h3><p>Sed ut perspiciatis omnis iste natus error sit amet</p>
  </div>
</section>

<h2 class="section-title" style="top:1874px">Our Work</h2>
<div class="work-card" style="left:65px;top:1994px"><div class="img" style="height:201px;background:linear-gradient(135deg,#f2c200,#f0a63c 60%,#e7c9d9)" role="img" aria-label="Printed floral gift boxes on a yellow backdrop"></div><p>Finibus Bonorum</p></div>
<div class="work-card" style="left:336px;top:2028px"><div class="img" style="height:275px;background:linear-gradient(160deg,#f4eef0,#e9d8cc 50%,#f7f4ef)" role="img" aria-label="Printed mug with a paper gift bag and flower"></div><p>Finibus Bonorum</p></div>
<div class="work-card" style="left:605px;top:1951px"><div class="img" style="height:276px;background:linear-gradient(160deg,#f6b51a,#f0a21a 55%,#b9733a)" role="img" aria-label="Printed greeting card beside stacked stones"></div><p>Finibus Bonorum</p></div>
<div class="work-card" style="left:875px;top:2060px"><div class="img" style="height:200px;background:linear-gradient(150deg,#e9edf0,#cfd8de 55%,#3a8fb5)" role="img" aria-label="Printed photo prints spread on a table"></div><p>Finibus Bonorum</p></div>

<section class="team" role="img" aria-label="Colour swatch fan in the background">
  <h2 class="section-title" style="top:42px;color:var(--white)">Our Team</h2>
  <div class="member" style="left:65px"><div class="img" style="background:linear-gradient(180deg,#e4e4e4,#8fa6a8)" role="img" aria-label="Portrait of team member"></div><h4>Tobin Alder</h4><span>Designer</span></div>
  <div class="member" style="left:336px"><div class="img" style="background:linear-gradient(180deg,#d9d2cc,#c9a27a)" role="img" aria-label="Portrait of team member"></div><h4>Mirela Vantosh</h4><span>Designer</span></div>
  <div class="member" style="left:607px"><div class="img" style="background:linear-gradient(180deg,#e6e3df,#3a3030)" role="img" aria-label="Portrait of team member"></div><h4>Lenora Brisk</h4><span>Maintenece</span></div>
  <div class="member" style="left:878px"><div class="img" style="background:linear-gradient(180deg,#c9cdd0,#2b2d31)" role="img" aria-label="Portrait of team member"></div><h4>Caspar Holme</h4><span>Lab Expert</span></div>
</section>

<h2 class="section-title" style="top:2980px">Testimonials</h2>
<p class="abs testi-text">Sed ut perspiciatis unde omnis iste natus error sit voluptatem accusantium doloremque laudantium, totam rem aperiam, eaque ipsa quae ab illo inventore veritatis et quasi architecto beatae vitae dicta sunt explicabo. Nemo enim ipsam voluptatem quia voluptas sit aspernatur aut odit aut fugit, sed quia consequuntur magni dolores eos qui ratione voluptatem sequi nesciunt.</p>
<div class="avatar" style="left:384px;top:3245px;width:80px;height:80px;background:#d8d8d8" role="img" aria-label="Customer portrait"></div>
<div class="avatar" style="left:546px;top:3231px;width:108px;height:108px;background:#b59a86" role="img" aria-label="Customer portrait"></div>
<div class="avatar" style="left:735px;top:3245px;width:80px;height:80px;background:#9c9c9c" role="img" aria-label="Customer portrait"></div>
<div class="abs" style="left:0;top:3356px;width:1200px;text-align:center;font-size:22px;font-weight:600">Dorian K. Welt</div>
<div class="abs" style="left:0;top:3388px;width:1200px;text-align:center;font-size:16px;color:var(--grey)">Customer</div>

<section class="newsletter">
  <h2 class="abs nl-title">Stay<br>Connected</h2>
  <p class="abs nl-sub">Subscribe to our Newsletter</p>
  <label class="abs nl-label">Enter Your Email:</label>
  <div class="abs nl-line"></div>
  <a class="abs btn nl-btn">Subscribe</a>
</section>

<footer class="footer">
  <h5 style="left:65px">VISIT US</h5>
  <div class="contact-row" style="top:108px"><svg width="14" height="18" viewBox="0 0 14 18"><path d="M7 0a7 7 0 0 1 7 7c0 5-7 11-7 11S0 12 0 7a7 7 0 0 1 7-7z" fill="var(--blue)"/><circle cx="7" cy="7" r="2.5" fill="var(--footer)"/></svg><span>87 Larkmoor Street, 3rd Floor<br>Fennbridge, OR 97012 USA</span></div>
  <div class="contact-row" style="top:190px"><svg width="14" height="16" viewBox="0 0 14 16"><path d="M3 1l3 3-2 2c1 2 3 4 5 5l2-2 3 3-2 3C6 15 0 9 1 3z" fill="var(--blue)"/></svg><span>+32 400 55 12 80</span></div>
  <div class="contact-row" style="top:243px"><svg width="16" height="12" viewBox="0 0 16 12"><rect width="16" height="12" fill="var(--blue)"/><path d="M0 0l8 7 8-7" fill="none" stroke="var(--footer)" stroke-width="1.5"/></svg><span>info@brimvelt.com</span></div>
  <div class="divider" style="left:418px"></div>
  <h5 style="left:481px">Quick Links</h5>
  <ul class="links"><li>Home</li><li>About Us</li><li>Work</li><li>Blog</li><li>Contact Us</li></ul>
  <div class="divider" style="left:693px"></div>
  <h5 style="left:755px">GET IN TOUCH</h5>
  <p class="abs touch-text">We are always ready to answer any questions you may have regarding our services.</p>
  <a class="abs outline-btn">Call Us</a>
  <a class="abs btn fill-btn">Contact Us</a>
</footer>

<div class="footer-bar">
  <div class="copy">© 2022 <b>Brimvelt</b>. Privacy Policy</div>
  <div class="social" style="left:993px"></div>
  <div class="social" style="left:1043px"></div>
  <div class="social" style="left:1093px"></div>
</div>

</body>
</html>
```